Billboard for personal injury chiropractors office

We are a personal injury chiropractor clinic.
I need a Billboard with the company name as the dominating factor. Also a smaller picture or 2 of something creative, like a car accident or an arm in a cast off to the sides.
We Like something Clean and Simple and Eye Catching. Please make the picture Small and Off To The Side. The MAIN FOCUS areas are the… name Pell Chiropractic Clinic
At the top CAR ACCIDENT INJURY?
AND at the bottom our number 581-47-TORSO.
Dr.Marla T. Pell in bold somewhere with the word chiropractor under the doctors name in a text.

Im open to red lettering on white backgrounds, red on yellow backgrounds and I'm also open to reds blues white and yellow. I'd prefer yellow if used be across the bottom.

I am uploading a very rough draft of what we are after along with a screenshot of the tv commercial showing the yellow

DO NOT USE THE LOGO ON THE COMMERCIAL. I JUST WANT THE NAME TYPED LIKE ON SAMPLE BILLBOARD.

Industry/Entity Type

Chiropractic

Colors
0054AA
0677BA
7BADD7
CADEEF
E8F1F8
FFF300
FFF600
FEFA6F
FFFEC7
FFFEE8
EB3D1F
EC4F4E
F09395
F8D3D4
FCEDEE

Requirements
Must have
• Eye catching ,bold

```html
<!DOCTYPE html>
<html lang="en">
<head>
<meta charset="utf-8">
<title>Pell Chiropractic Clinic Billboard</title>
<link href="https://fonts.googleapis.com/css2?family=Bebas+Neue&family=Oswald:wght@200&family=Poppins:wght@600;700&display=swap" rel="stylesheet">
<style>
  :root {
    --page: #161616;
    --board: #ffffff;
    --ink: #111111;
    --red: #c6000b;
    --yellow: #fff300;
    --suit: #2f333c;
    --shirt: #dfe6ee;
  }
  * { margin: 0; padding: 0; box-sizing: border-box; }
  html, body {
    width: 1200px;
    height: 1200px;
    overflow: hidden;
    background: var(--page);
  }
  .billboard {
    position: absolute;
    left: 99px;
    top: 454px;
    width: 1002px;
    height: 292px;
    background: var(--board);
    overflow: hidden;
  }
  .headline {
    position: absolute;
    left: 40px;
    top: 17px;
    font-family: "Oswald", sans-serif;
    font-weight: 200;
    font-size: 72px;
    line-height: 1;
    letter-spacing: -3px;
    color: var(--ink);
    white-space: nowrap;
  }
  .clinic-name {
    position: absolute;
    left: 40px;
    top: 96px;
    font-family: "Bebas Neue", sans-serif;
    font-weight: 400;
    font-size: 88px;
    line-height: 1;
    letter-spacing: 1px;
    color: var(--red);
    white-space: nowrap;
    z-index: 2;
  }
  .doctor-name {
    position: absolute;
    left: 40px;
    top: 183px;
    font-family: "Poppins", sans-serif;
    font-weight: 600;
    font-size: 44px;
    line-height: 1.2;
    color: var(--red);
    white-space: nowrap;
  }
  .call-band {
    position: absolute;
    left: 0;
    top: 236px;
    width: 726px;
    height: 56px;
    background: var(--yellow);
    clip-path: polygon(0 0, 100% 0, 98% 100%, 0 100%);
    display: flex;
    align-items: center;
    padding-left: 104px;
    font-family: "Poppins", sans-serif;
    color: var(--ink);
    white-space: nowrap;
  }
  .call-label {
    font-weight: 600;
    font-size: 24px;
    margin-right: 10px;
  }
  .call-number {
    font-weight: 700;
    font-size: 42px;
    letter-spacing: 0.5px;
  }
  .doctor-photo {
    position: absolute;
    right: 0;
    top: 6px;
    width: 228px;
    height: 286px;
    background: linear-gradient(180deg, #ffffff 0%, var(--shirt) 45%, var(--suit) 100%);
  }
</style>
</head>
<body>
  <section class="billboard">
    <h2 class="headline">CAR ACCIDENT INJURY?</h2>
    <h1 class="clinic-name">PELL CHIROPRACTIC CLINIC</h1>
    <p class="doctor-name">Dr.Marla T. Pell</p>
    <div class="call-band">
      <span class="call-label">Call Now</span>
      <span class="call-number">581-555-0147</span>
    </div>
    <div class="doctor-photo" role="img" aria-label="Portrait photo of the doctor in a dark blazer and light shirt"></div>
  </section>
</body>
</html>
```